Talvin Foundation Letterhead

We are a newly established non profit registered in Maryland but operates in Africa, south of the sahara. We offer scholarships to deserving young adults from high school through college. Our color theme for our existing logo is purple, we want a design that is stylish, spellbinding yet a letterhead that projects seriousness. More information on www.thetalvinfoundation.org

Target Market(s)

High school and college students in sub saharan African as well as our donors in the US

Industry/Entity Type

Non Profit

Font styles to use
Script

Requirements
Must have
• Logo at the top and if possible watermark the logo in the middle of the letterhead, contact address,
Should not have
• NA

```html
<!DOCTYPE html>
<html lang="en">
<head>
<meta charset="utf-8">
<title>Talvin Foundation Letterhead</title>
<link href="https://fonts.googleapis.com/css2?family=Didact+Gothic&display=swap" rel="stylesheet">
<style>
  :root {
    --backdrop: #e4e4e6;
    --paper: #f7f7f7;
    --purple: #7d5594;
    --purple-deep: #7a4f91;
    --purple-light: #a8a3cc;
    --band-grey: #dcdcdc;
    --ring-grey: #d4d4d6;
    --watermark: #e9e9ea;
    --text-grey: #6a6a6a;
  }
  html, body {
    margin: 0;
    width: 1200px;
    height: 991px;
    overflow: hidden;
    background: var(--backdrop);
  }
  .letterhead {
    position: absolute;
    left: 262px;
    top: 20px;
    width: 676px;
    height: 951px;
    background: var(--paper);
    box-shadow: 0 1px 4px rgba(0,0,0,0.18);
    overflow: hidden;
  }
  .side-band {
    position: absolute;
    left: 0; top: 0;
    width: 32px; height: 100%;
    background: linear-gradient(to bottom, var(--purple-deep) 0%, var(--purple-light) 50%, var(--purple-deep) 100%);
  }
  .side-rule {
    position: absolute;
    left: 32px; top: 0;
    width: 13px; height: 100%;
    background: var(--band-grey);
  }
  .brand-mark {
    position: absolute;
    left: 8px; top: 31px;
    width: 56px; height: 56px;
    border-radius: 50%;
    background: var(--paper);
    border: 3px solid var(--ring-grey);
  }
  .brand-name {
    position: absolute;
    left: 88px; top: 48px;
    margin: 0;
    color: var(--purple);
    font-family: "Didact Gothic", sans-serif;
    font-weight: 400;
    font-size: 21px;
    line-height: 1;
    white-space: nowrap;
  }
  .watermark {
    position: absolute;
    left: 136px; top: 288px;
    width: 412px; height: 412px;
    border-radius: 50%;
    border: 11px solid var(--watermark);
    display: flex;
    align-items: center;
    justify-content: center;
  }
  .watermark-name {
    color: var(--watermark);
    font-family: "Didact Gothic", sans-serif;
    font-size: 34px;
    white-space: nowrap;
  }
  .contact-tab {
    position: absolute;
    left: 0; top: 872px;
    width: 50px; height: 56px;
    background: var(--purple);
    border-radius: 0 8px 8px 0;
  }
  .contact-icons {
    position: absolute;
    left: 36px; top: 879px;
    width: 10px;
  }
  .contact-icons svg { display: block; margin-bottom: 4px; }
  .contact-lines, .address-lines {
    position: absolute;
    margin: 0;
    font-family: "Didact Gothic", sans-serif;
    font-style: normal;
    font-size: 10px;
    line-height: 12.5px;
    color: var(--text-grey);
  }
  .contact-lines { left: 58px; top: 874px; }
  .address-lines { right: 38px; top: 886px; text-align: right; }
</style>
</head>
<body>
  <main class="letterhead">
    <div class="side-band"></div>
    <div class="side-rule"></div>

    <header>
      <div class="brand-mark"></div>
      <h1 class="brand-name">Talvin Foundation Inc</h1>
    </header>

    <div class="watermark" aria-hidden="true">
      <span class="watermark-name">Talvin Foundation</span>
    </div>

    <footer>
      <div class="contact-tab"></div>
      <div class="contact-icons" aria-hidden="true">
        <svg width="10" height="10" viewBox="0 0 10 10"><path d="M2.5 1 L4 3 L3 4 Q4 6 6 7 L7 6 L9 7.5 L8 9 Q2 8 1 2 Z" fill="#fff"/></svg>
        <svg width="10" height="10" viewBox="0 0 10 10"><rect x="1" y="2.5" width="8" height="5.5" fill="none" stroke="#fff" stroke-width="1"/><path d="M1 2.5 L5 5.5 L9 2.5" fill="none" stroke="#fff" stroke-width="1"/></svg>
        <svg width="10" height="10" viewBox="0 0 10 10"><circle cx="5" cy="5" r="3.8" fill="none" stroke="#fff" stroke-width="0.9"/><ellipse cx="5" cy="5" rx="1.6" ry="3.8" fill="none" stroke="#fff" stroke-width="0.8"/><path d="M1.2 5 H8.8" stroke="#fff" stroke-width="0.8"/></svg>
      </div>
      <address class="contact-lines">
        (416) 555-0142<br>
        info@thetalvinfoundation.org<br>
        www.thetalvinfoundation.org
      </address>
      <address class="address-lines">
        240 Maple Crest Rd - Unit 12<br>
        Toronto, ON Canada, M4C 2X5
      </address>
    </footer>
  </main>
</body>
</html>
```